Private Gym Needs a Rack Card Design

We need a basic front and back rack card (same size as post card) that gives basic information about our brand, and includes our logo. Please see attached logo and required content below.

Target Market(s)

Upscale, private gym.

Industry/Entity Type

Gym

Font styles to use
Sans Serif

Colors
ffffff
5c5c5c
000000
dbdbdb
f78f20

Requirements
Must have
• Business Logo and the following text in a clean, modern, easy-to-read, artistic manner. Style and design must be clean, incorporate our color scheme of MOSTLY white, light grey, charcoal, with just pops of orange. We want the card itself to be mostly white background. Must include website URL as well: corevaultfitness.com
• FRONT CARD:
• Logo
• A safe and individualized approach to exercise
• our path employs the latest weight resistance training exercises and coaching for healthy living. Not only is our workout methodology effective, it’s safe.
• Our Path…
• -Improves Functional Movement
• -Promotes Weight Loss
• -Builds Strength
• -Increases Flexibility 

• BACK:
• Change Your Body. Find Your Strength.
• There’s 40 years of success behind our proven method
• What is Iron Path? 
• Iron Path is all about teaching our clients how to lift weights and exercise with the proper technique. There’s no slinging or jerking at our gym; only controlled movements that yield real results.
• Come workout with us in our private gym. We are located in Durham adjacent to Larch Campus and 5 minutes from downtown Durham.
• Address: 482 Fenwick Ave, Durham, NC 27705
• Phone: (919) 555-0147
• Hours: 9:00 AM – 9:00 PM
Nice to have
• Great organization of text, maybe some columns, colored bullet points, cool graphics and logos.
Should not have
• Busy or crowded design. All lines should be sleek, straight, and streamline. NO STOCK IMAGES, but logos are GREAT

```html
<!DOCTYPE html>
<html lang="en">
<head>
<meta charset="utf-8">
<title>Iron Path — Rack Card Front</title>
<link rel="stylesheet" href="https://fonts.googleapis.com/css2?family=Arimo&family=PT+Sans:wght@400;700&display=swap">
<style>
  :root {
    --white: #ffffff;
    --charcoal: #5c5c5c;
    --light-grey: #f2f2f2;
    --orange: #f78f20;
    --text: #55565a;
  }
  * { margin: 0; padding: 0; box-sizing: border-box; }
  html, body { width: 1200px; height: 900px; overflow: hidden; }
  body { background: var(--light-grey); position: relative; font-family: "PT Sans", sans-serif; }

  .rack-card {
    position: absolute; left: 170px; top: 175px;
    width: 860px; height: 614px;
    background: var(--white);
  }
  .brand {
    position: absolute; top: 48px; left: 0; width: 100%;
    text-align: center;
    font-family: "PT Sans", sans-serif; font-weight: 700;
    font-size: 40px; letter-spacing: 1px; color: var(--charcoal);
    text-transform: uppercase;
  }
  .headline {
    position: absolute; top: 123px; left: 0; width: 100%;
    text-align: center;
    font-family: "Arimo", sans-serif; font-size: 27px; line-height: 33px;
    color: var(--text);
  }
  .headline .accent { color: var(--orange); }
  .intro {
    position: absolute; top: 203px; left: 0; width: 100%;
    text-align: center; font-size: 20px; line-height: 26px; color: var(--text);
  }
  .lead-in {
    position: absolute; top: 302px; left: 0; width: 100%;
    text-align: center; font-size: 20px; color: var(--orange);
  }
  .benefit-band {
    position: absolute; top: 349px; left: 0; width: 100%; height: 127px;
    background: var(--charcoal);
    border-top: 8px solid var(--orange);
    border-bottom: 8px solid var(--orange);
  }
  .benefit-icon { position: absolute; top: 23px; width: 68px; height: 68px; }
  .benefit-label {
    position: absolute; top: 488px;
    font-size: 20px; line-height: 26px; color: var(--orange);
  }
</style>
</head>
<body>
  <main class="rack-card">
    <div class="brand">Iron Path</div>

    <h1 class="headline">A SAFE AND INDIVIDUALIZED<br><span class="accent">APPROACH TO EXERCISE</span></h1>

    <p class="intro">Our path employs the latest<br>weight resistance training exercises and coaching for healthy living.<br>Not only is our workout methodology effective, it’s safe.</p>

    <p class="lead-in">Our Path...</p>

    <section class="benefit-band">
      <svg class="benefit-icon" style="left:117px" viewBox="0 0 68 68">
        <rect x="2.5" y="2.5" width="63" height="63" rx="6" fill="none" stroke="#fff" stroke-width="4"/>
        <rect x="14" y="14" width="40" height="40" rx="3" fill="#8a8a8a" role="img" aria-label="Running figure icon"/>
      </svg>
      <svg class="benefit-icon" style="left:298px" viewBox="0 0 68 68">
        <rect x="2.5" y="2.5" width="63" height="63" rx="6" fill="none" stroke="#fff" stroke-width="4"/>
        <path d="M12 22 Q34 8 56 22 L50 32 Q34 24 18 32 Z" fill="#fff"/>
        <line x1="34" y1="30" x2="34" y2="58" stroke="#fff" stroke-width="5" stroke-linecap="round"/>
      </svg>
      <svg class="benefit-icon" style="left:480px" viewBox="0 0 68 68">
        <rect x="2.5" y="2.5" width="63" height="63" rx="6" fill="none" stroke="#fff" stroke-width="4"/>
        <rect x="12" y="22" width="5" height="24" fill="#fff"/>
        <rect x="19" y="18" width="6" height="32" fill="#fff"/>
        <rect x="25" y="31" width="18" height="6" fill="#fff"/>
        <rect x="43" y="18" width="6" height="32" fill="#fff"/>
        <rect x="51" y="22" width="5" height="24" fill="#fff"/>
      </svg>
      <svg class="benefit-icon" style="left:662px" viewBox="0 0 68 68">
        <rect x="2.5" y="2.5" width="63" height="63" rx="6" fill="none" stroke="#fff" stroke-width="4"/>
        <g fill="none" stroke="#fff" stroke-width="4">
          <path d="M34 20 V34"/>
          <path d="M36 56 V44 Q36 34 48 28"/>
          <path d="M28 42 Q24 32 18 28"/>
        </g>
        <g fill="#fff">
          <path d="M34 10 L41 21 H27 Z"/>
          <path d="M54 24 L44 23 L50 33 Z"/>
          <path d="M13 24 L23 23 L17 33 Z"/>
        </g>
      </svg>
    </section>

    <p class="benefit-label" style="left:118px">Improves<br>Functional<br>Movement</p>
    <p class="benefit-label" style="left:299px;top:491px">Promotes<br>Weight<br>Loss</p>
    <p class="benefit-label" style="left:480px">Builds<br>Strength</p>
    <p class="benefit-label" style="left:662px;top:486px">Increases<br>Flexibility</p>
  </main>
</body>
</html>
```